LLC needs a business card design that emphasizes consulting and expert witness in upstream oil and g

I need a business card design for my company called Velmo Consultative Service, LLC. My expertise is in oil and gas upstream operations management to optimize performance and also as an expert witness for law firms in oil and gas upstream operations litigation.
The final design should communicate knowledge and hands-on experience as well as trust. (Velmo means rope or lasso. Perhaps "Velmo" should be in the form of a rope.) I do not like the color green in any shade. My first preference would be some shade of blue.

```html
<!DOCTYPE html>
<html lang="en">
<head>
<meta charset="utf-8">
<title>Velmo Consultative Service, LLC — Business Card</title>
<link rel="stylesheet" href="https://fonts.googleapis.com/css2?family=Open+Sans:wght@400;600;700&display=swap">
<style>
  :root {
    --page-bg: #eeeeee;
    --card-bg: #ffffff;
    --brand-blue: #0a64a4;
    --brand-blue-light: #0b84b8;
    --brand-orange: #e8792c;
    --ink-white: #ffffff;
  }
  * { margin: 0; padding: 0; box-sizing: border-box; }
  html, body {
    width: 1200px; height: 1000px; overflow: hidden;
    background: var(--page-bg);
    font-family: "Open Sans", Arial, sans-serif;
  }
  .canvas { position: relative; width: 1200px; height: 1000px; }
  .card {
    position: absolute;
    background: var(--card-bg);
    overflow: hidden;
    box-shadow: 0 6px 18px rgba(0,0,0,0.18);
  }
  .card-front { left: 140px; top: 150px; width: 650px; height: 380px; }
  .card-back  { left: 420px; top: 570px; width: 660px; height: 340px; }

  /* Front: straight horizontal bands */
  .front-rule {
    position: absolute; left: 0; right: 0; top: 214px; height: 8px;
    background: var(--brand-orange);
  }
  .front-band {
    position: absolute; left: 0; right: 0; top: 230px; bottom: 0;
    background: linear-gradient(180deg, var(--brand-blue-light), var(--brand-blue));
  }

  /* Back: straight vertical bands */
  .back-band {
    position: absolute; left: 0; top: 0; bottom: 0; width: 96px;
    background: linear-gradient(180deg, var(--brand-blue-light), var(--brand-blue));
  }
  .back-rule {
    position: absolute; left: 104px; top: 0; bottom: 0; width: 8px;
    background: var(--brand-orange);
  }

  .wordmark { position: absolute; color: var(--brand-blue); }
  .wordmark-name {
    display: block; font-weight: 700; letter-spacing: 2px; line-height: 1;
  }
  .wordmark-tagline {
    display: block; font-weight: 400; letter-spacing: 1.5px; text-transform: uppercase;
  }
  .card-front .wordmark { left: 50px; top: 42px; }
  .card-front .wordmark-name { font-size: 58px; }
  .card-front .wordmark-tagline { font-size: 16px; margin-top: 8px; }
  .card-back .wordmark { left: 180px; top: 100px; }
  .card-back .wordmark-name { font-size: 70px; }
  .card-back .wordmark-tagline { font-size: 19px; margin-top: 10px; }

  .person { position: absolute; left: 56px; top: 252px; color: var(--ink-white); }
  .person-name { font-size: 18px; font-weight: 400; }
  .person-title { font-size: 13px; font-weight: 600; margin-top: 4px; }

  .contacts {
    position: absolute; left: 60px; top: 312px;
    display: grid; grid-template-columns: 175px auto; row-gap: 10px;
    color: var(--ink-white); font-size: 15px; list-style: none;
  }
  .contact-label {
    color: var(--brand-orange); font-weight: 700;
    display: inline-block; width: 22px;
  }
</style>
</head>
<body>
<main class="canvas">

  <section class="card card-front" aria-label="Business card front">
    <div class="front-rule" aria-hidden="true"></div>
    <div class="front-band" aria-hidden="true"></div>
    <div class="wordmark">
      <span class="wordmark-name">VELMO</span>
      <span class="wordmark-tagline">Consultative Service, LLC</span>
    </div>
    <div class="person">
      <p class="person-name">Daniel Harwick</p>
      <p class="person-title">Director &amp; Operations Manager</p>
    </div>
    <ul class="contacts">
      <li><span class="contact-label">O</span>555.214.0381</li>
      <li><span class="contact-label">E</span>daniel@velmo.com</li>
      <li><span class="contact-label">M</span>555.706.4192</li>
      <li><span class="contact-label">W</span>www.velmo.com</li>
    </ul>
  </section>

  <section class="card card-back" aria-label="Business card back">
    <div class="back-band" aria-hidden="true"></div>
    <div class="back-rule" aria-hidden="true"></div>
    <div class="wordmark">
      <span class="wordmark-name">VELMO</span>
      <span class="wordmark-tagline">Consultative Service, LLC</span>
    </div>
  </section>

</main>
</body>
</html>
```